Real estate investor, needing a business card that communicates warmth, integrity, empathy.

I have a logo that can be manipulated to align with the message - "Here to help you move forward." Want it to stand out from typical real estate investor cards, and make distressed home sellers feel a connection with me. Should communicate warmth, integrity, empathy, and trustworthiness.

Target Market(s)

Distressed home owners who need to sell their homes, not using realtors.

Contact Information for Business Card

Glossy front and matte back, with a small box that is labelled "notes." I like darker blues and blacks together, but doesn't have to be, as long as it communicates trustworthiness, and a strong call to action.

Other font styles liked:
• see "must haves" above, but willing to review whatever comes my way.

Requirements
Must have
• The fonts on my logo are Aviano, Lusitana, and Marcellus. We don't have to use those, but I favor them.

```html
<!DOCTYPE html>
<html lang="en">
<head>
<meta charset="utf-8">
<title>Ridgeline Property Partners – Business Card</title>
<link href="https://fonts.googleapis.com/css2?family=Roboto:wght@300;400;500&display=swap" rel="stylesheet">
<style>
  :root {
    --backdrop: #1e1c1d;
    --card-navy: #1a2642;
    --ink-white: #ffffff;
    --ink-soft: #e6e9f0;
  }
  * { box-sizing: border-box; margin: 0; padding: 0; }
  html, body { width: 1200px; height: 1200px; overflow: hidden; }
  body {
    background: var(--backdrop);
    display: flex;
    flex-direction: column;
    align-items: center;
    justify-content: center;
    gap: 56px;
    font-family: "Roboto", Arial, sans-serif;
  }
  .card {
    position: relative;
    width: 860px;
    height: 491px;
    background: var(--card-navy);
    border-radius: 26px;
    color: var(--ink-white);
    overflow: hidden;
  }
  .brand-name {
    font-family: "Roboto", Arial, sans-serif;
    font-weight: 500;
    color: var(--ink-white);
    letter-spacing: 1px;
    line-height: 1.15;
  }
  .brand-tagline {
    font-family: "Roboto", Arial, sans-serif;
    font-weight: 300;
    font-size: 12px;
    letter-spacing: 2px;
    color: var(--ink-soft);
    margin-top: 16px;
  }

  /* Back card – notes side */
  .card-back .brand {
    position: absolute;
    right: 110px;
    top: 130px;
    text-align: center;
  }
  .card-back .brand-name { font-size: 38px; }
  .notes {
    position: absolute;
    left: 390px;
    right: 60px;
    bottom: 110px;
    display: flex;
    align-items: flex-end;
    gap: 14px;
  }
  .notes-label {
    font-weight: 500;
    font-size: 15px;
    letter-spacing: .5px;
  }
  .notes-box {
    flex: 1;
    height: 34px;
    background: var(--ink-white);
  }

  /* Front card – contact side */
  .card-front .brand {
    position: absolute;
    left: 90px;
    top: 170px;
  }
  .card-front .brand-name { font-size: 40px; }
  .contact {
    position: absolute;
    right: 54px;
    top: 110px;
    text-align: right;
  }
  .person-name { font-size: 30px; font-weight: 500; letter-spacing: .5px; }
  .person-role { font-size: 16px; font-weight: 300; margin-bottom: 28px; }
  .address { font-size: 16px; font-weight: 300; margin-bottom: 18px; }
  .contact-line {
    display: flex;
    justify-content: flex-end;
    align-items: center;
    gap: 10px;
    font-size: 17px;
    font-weight: 300;
    line-height: 1.5;
  }
  .contact-line svg { width: 15px; height: 15px; fill: none; stroke: var(--ink-white); stroke-width: 1.6; }
</style>
</head>
<body>

  <section class="card card-back" aria-label="Card back with notes box">
    <div class="brand">
      <div class="brand-name">RIDGELINE<br>PROPERTY PARTNERS</div>
      <p class="brand-tagline">- Here to help you move forward -</p>
    </div>
    <div class="notes">
      <span class="notes-label">NOTES</span>
      <span class="notes-box"></span>
    </div>
  </section>

  <section class="card card-front" aria-label="Card front with contact details">
    <div class="brand">
      <div class="brand-name">RIDGELINE<br>PROPERTY PARTNERS</div>
    </div>
    <div class="contact">
      <p class="person-name">MARCUS HALE</p>
      <p class="person-role">Principal Broker</p>
      <p class="address">1480 Birchwood Lane Fairbanks, AK 99701</p>
      <p class="contact-line">555.210.4477
        <svg viewBox="0 0 16 16" aria-hidden="true"><path d="M4 2l2 3-1.5 1.5a8 8 0 0 0 5 5L11 10l3 2-1 2.5C7 14 2 9 1.5 3z"/></svg>
      </p>
      <p class="contact-line">555.210.4478
        <svg viewBox="0 0 16 16" aria-hidden="true"><rect x="4.5" y="1.5" width="7" height="13" rx="1.2"/><line x1="7" y1="12.5" x2="9" y2="12.5"/></svg>
      </p>
      <p class="contact-line">hello@ridgelinehomes.com
        <svg viewBox="0 0 16 16" aria-hidden="true"><rect x="1.5" y="3.5" width="13" height="9" rx="1"/><path d="M1.5 4l6.5 5 6.5-5"/></svg>
      </p>
      <p class="contact-line">www.ridgelinehomes.com
        <svg viewBox="0 0 16 16" aria-hidden="true"><circle cx="8" cy="8" r="6.5"/><ellipse cx="8" cy="8" rx="3" ry="6.5"/><line x1="1.5" y1="8" x2="14.5" y2="8"/></svg>
      </p>
    </div>
  </section>

</body>
</html>
```